Business cards for a naturopathic day clinic for stem cell therapy

We need a basic design for a day clinic, that offers stem cell therapies for Lyme therapy and other severe chronic illnesses.
Our name is "Casa velorìn", which can be translated into "Manor Velorbloom". We are a couple of naturopaths working along side physiotherapists and osteopaths, yoga teachers and massage therapists. I attached our logo.

```html
<!DOCTYPE html>
<html lang="en">
<head>
<meta charset="utf-8">
<title>Casa velorìn — Business Cards</title>
<link rel="stylesheet" href="https://fonts.googleapis.com/css2?family=Poppins:wght@300;400;500&display=swap">
<style>
  :root{
    --taupe:#9b8877;
    --taupe-deep:#8a7565;
    --leaf:#b4c45a;
    --paper:#ffffff;
    --backdrop:#2b2b2b;
  }
  *{margin:0;padding:0;box-sizing:border-box}
  html,body{width:1200px;height:900px;overflow:hidden;background:var(--backdrop)}
  body{font-family:"Poppins",sans-serif;position:relative}
  .card{position:absolute;left:250px;width:700px;height:400px;border-radius:26px;overflow:hidden}
  .card--back{top:35px;background:var(--taupe)}
  .card--front{top:465px;background:var(--paper)}

  .back-pattern{position:absolute;inset:0;background:linear-gradient(135deg,#a08d7c,#958271)}
  .back-brand{position:absolute;right:70px;bottom:70px;display:flex;align-items:center;gap:12px;color:var(--paper);font-size:34px;font-weight:300;letter-spacing:1px}
  .brand-dot{width:34px;height:34px;border-radius:50%;border:2px solid currentColor;flex:none}

  .front-waves{position:absolute;inset:0;width:700px;height:400px}
  .front-brand{position:absolute;left:48px;top:70px;display:flex;align-items:center;gap:16px;color:var(--taupe-deep);font-size:46px;font-weight:300;letter-spacing:1px}
  .front-brand .brand-dot{width:50px;height:50px;border-color:var(--leaf);border-width:3px}
  .services{position:absolute;right:52px;top:42px;text-align:right;color:var(--taupe-deep);font-size:15px;line-height:1.5;font-weight:400}
  .address{position:absolute;left:60px;top:200px;display:flex;gap:12px;color:var(--taupe-deep);font-size:19px;line-height:1.45}
  .address svg{margin-top:10px;flex:none}
  .contacts{position:absolute;right:48px;top:218px;list-style:none;color:var(--paper);font-size:16px;line-height:1.75}
  .contacts li{display:flex;justify-content:flex-end;align-items:center;gap:10px}
  .contacts svg{flex:none}
</style>
</head>
<body>

<section class="card card--back" aria-label="Card back">
  <div class="back-pattern" role="img" aria-label="Faint repeating brand-name pattern in tone-on-tone taupe"></div>
  <div class="back-brand"><span class="brand-dot"></span><span>Casa velorìn</span></div>
</section>

<section class="card card--front" aria-label="Card front">
  <svg class="front-waves" viewBox="0 0 700 400" aria-hidden="true">
    <path d="M700,120 C590,118 520,190 450,255 C370,330 200,368 0,350 L0,400 L700,400 Z" fill="var(--taupe)"/>
    <path d="M0,322 C170,352 330,320 420,250 C460,218 495,185 525,165 C480,205 450,245 400,285 C300,355 150,358 0,340 Z" fill="var(--leaf)"/>
    <path d="M180,318 C300,310 380,270 440,215 C470,188 500,165 530,150 C490,185 460,222 420,256 C350,305 270,320 180,318 Z" fill="var(--taupe)"/>
  </svg>

  <div class="front-brand"><span class="brand-dot"></span><span>Casa velorìn</span></div>

  <p class="services">Physiotherapists and osteopaths<br>Yoga teachers and massage therapists</p>

  <div class="address">
    <svg width="16" height="20" viewBox="0 0 16 20"><path d="M8 1a6 6 0 0 0-6 6c0 4.5 6 11 6 11s6-6.5 6-11a6 6 0 0 0-6-6z" fill="none" stroke="var(--leaf)" stroke-width="2.4"/><circle cx="8" cy="7" r="2" fill="var(--leaf)"/></svg>
    <p>118 Alder Crest Road<br>Suite 210, Larkfield,<br>MI 49620</p>
  </div>

  <ul class="contacts">
    <li>555-302-4718
      <svg width="16" height="16" viewBox="0 0 16 16"><path d="M3 1.5l3 .5 1 3-2 1.5a9 9 0 0 0 4.5 4.5L11 9l3 1 .5 3c-1 1.5-3 2-5 1A13 13 0 0 1 1.5 6.5c-1-2-.5-4 1.5-5z" fill="var(--leaf)"/></svg></li>
    <li>ines@casavelorin.com
      <svg width="16" height="12" viewBox="0 0 16 12"><rect x="0.5" y="0.5" width="15" height="11" fill="var(--leaf)"/><path d="M1 1l7 6 7-6" fill="none" stroke="var(--taupe)" stroke-width="1.2"/></svg></li>
    <li>www.casavelorin.com
      <svg width="16" height="16" viewBox="0 0 16 16" fill="none" stroke="var(--leaf)" stroke-width="1.4"><circle cx="8" cy="8" r="7"/><ellipse cx="8" cy="8" rx="3" ry="7"/><path d="M1 8h14M2.5 4.5h11M2.5 11.5h11"/></svg></li>
  </ul>
</section>

</body>
</html>
```